Scientific project description

Here is a project description related to cellular mechanics, showing above the forces acting on cells in the tissues of our body. The forces on single cells are there to depict how forces are acting on cells (pressure squeezes the cell, shear flow is pushing the upward parts of the cell, tension pulls one part of the cell, strain is stretching the whole cell; the single cell images are to be found also on the last page). Intense red/purple are used to indicate that the forces are stressful (the colors to be used do not need to be exactly like these colors). The picture in the middle is a view of cells (same picture on next page if that needs to be modified). At the left, a description of what happens when everything is going well, i.e. the body stays healthy. At the right, if you dysfunction you get disease. Green nuances were used to indicate health, brownish, perhaps not so pleasant nuances were used to indicate disease. Below are the steps of the project.

On the whole, we're rather happy with the concept description as such, but it should look a little bit nicer. To many color nuances give a "noisy" impression, fonts could be nicer, layout more crisp, and the text on the steps should be more readable. We would also like to have two versions of the same picture, one with black background, one with white.

Target Market(s)

Scientists that are evaluating our project

Requirements
Must have
• Easy to grasp the idea, easy to read and understand the underlying idea.
Nice to have
• Would be good to have the Concept title ("Vorlint Concept and Envisioned Project Progression) on top of the figure as indicated in the second brief picture submitted.

```html
<!DOCTYPE html>
<html lang="en">
<head>
<meta charset="utf-8">
<title>Vorlint Concept and Envisioned Project Progression</title>
<link rel="stylesheet" href="https://fonts.googleapis.com/css2?family=Dosis:wght@500;600;700&display=swap">
<style>
  :root {
    --bg: #030505;
    --ink: #ffffff;
    --ink-dark: #1f2a2a;
    --pressure: #a52127;
    --pressure-soft: #b8464b;
    --shear: #8e1a2c;
    --shear-soft: #a3434f;
    --tension: #7f1a1f;
    --tension-soft: #964247;
    --strain: #722673;
    --strain-soft: #8a4b8b;
    --fit: #1e3a22;
    --frail: #8a3f1e;
    --health: #3db884;
    --disease: #f5af84;
    --step: #eef6f8;
    --step-edge: #6b7272;
    --cells-deep: #0c1a0c;
    --cells-mid: #2f7a2a;
  }
  html, body {
    margin: 0;
    padding: 0;
    overflow: hidden;
    background: var(--bg);
  }
  .canvas {
    position: relative;
    width: 1200px;
    height: 666px;
    background: var(--bg);
    font-family: "Dosis", sans-serif;
    overflow: hidden;
  }
  .figure { display: block; }
  .title {
    fill: var(--ink);
    font-size: 36px;
    font-weight: 600;
    letter-spacing: 0.6px;
  }
  .force-label, .flow-label, .machinery-label, .forces-caption {
    fill: var(--ink);
    font-weight: 500;
  }
  .force-label { font-size: 21px; letter-spacing: 0.8px; }
  .forces-caption { font-size: 22px; }
  .flow-label { font-size: 21px; }
  .machinery-label { font-size: 22px; letter-spacing: 0.9px; }
  .outcome-label { font-size: 22px; font-weight: 500; fill: var(--ink-dark); letter-spacing: 1px; }
  .hub-label {
    fill: var(--ink);
    font-size: 26px;
    font-weight: 700;
    letter-spacing: 2px;
  }
  .arrow-line { stroke: var(--ink); stroke-width: 3.5; }
  .arrow-head { fill: var(--ink); }
  .step-box { fill: var(--step); }
  .step-edge { fill: var(--step-edge); }
  .step-label { fill: var(--ink-dark); font-size: 20px; font-weight: 500; letter-spacing: 1.2px; }
</style>
</head>
<body>
<div class="canvas">
<svg class="figure" width="1200" height="666" viewBox="0 0 1200 666" xmlns="http://www.w3.org/2000/svg">
  <defs>
    <radialGradient id="cells-fill" cx="50%" cy="45%" r="55%">
      <stop offset="0%" stop-color="var(--cells-mid)"/>
      <stop offset="55%" stop-color="#24561f"/>
      <stop offset="100%" stop-color="var(--cells-deep)"/>
    </radialGradient>
  </defs>

  <text class="title" x="580" y="55" text-anchor="middle">Vorlint Concept and Envisioned Project Progression</text>

  <g class="force-band">
    <polygon points="211,72 415,72 415,174 211,204" fill="var(--pressure)"/>
    <rect x="415" y="72" width="168" height="102" fill="var(--shear)"/>
    <rect x="583" y="72" width="168" height="102" fill="var(--tension)"/>
    <polygon points="751,72 955,72 955,204 751,174" fill="var(--strain)"/>

    <text class="force-label" x="307" y="96" text-anchor="middle">Pressure</text>
    <text class="force-label" x="499" y="96" text-anchor="middle">Shear</text>
    <text class="force-label" x="661" y="96" text-anchor="middle">Tension</text>
    <text class="force-label" x="847" y="96" text-anchor="middle">Strain</text>

    <rect x="256" y="104" width="112" height="66" rx="8" fill="var(--pressure-soft)" role="img" aria-label="Cell squeezed flat by downward pressure arrows"/>
    <rect x="462" y="102" width="88" height="62" rx="8" fill="var(--shear-soft)" role="img" aria-label="Cell pushed sideways by shear flow arrows"/>
    <rect x="620" y="102" width="82" height="60" rx="8" fill="var(--tension-soft)" role="img" aria-label="Cell pulled upward at one point by tension arrows"/>
    <rect x="763" y="118" width="180" height="40" rx="8" fill="var(--strain-soft)" role="img" aria-label="Cell stretched lengthwise by outward strain arrows"/>
  </g>

  <text class="forces-caption" x="894" y="222" text-anchor="middle">Forces on cells</text>

  <circle cx="582" cy="298" r="127" fill="url(#cells-fill)" role="img" aria-label="Fluorescence microscopy view of cells with green cytoskeleton and red adhesion sites"/>
  <text class="hub-label" x="582" y="301" text-anchor="middle">Mechanostasis</text>

  <text class="flow-label" x="404" y="282" text-anchor="middle">Cell fitness</text>
  <line class="arrow-line" x1="438" y1="294" x2="366" y2="294"/>
  <polygon class="arrow-head" points="355,294 369,286 369,302"/>

  <circle cx="273" cy="306" r="74" fill="var(--fit)"/>
  <text class="machinery-label" text-anchor="middle">
    <tspan x="273" y="290">Functional</tspan>
    <tspan x="273" y="314">cellular</tspan>
    <tspan x="273" y="338">machineries</tspan>
  </text>
  <line class="arrow-line" x1="273" y1="384" x2="273" y2="404"/>
  <polygon class="arrow-head" points="273,415 265,402 281,402"/>
  <circle cx="273" cy="470" r="52" fill="var(--health)"/>
  <text class="outcome-label" x="273" y="477" text-anchor="middle">Health</text>

  <text class="flow-label" x="760" y="282" text-anchor="middle">Cell frailty</text>
  <line class="arrow-line" x1="718" y1="294" x2="796" y2="294"/>

  <circle cx="894" cy="306" r="74" fill="var(--frail)"/>
  <text class="machinery-label" text-anchor="middle">
    <tspan x="894" y="290">Dysfunctional</tspan>
    <tspan x="894" y="314">cellular</tspan>
    <tspan x="894" y="338">machineries</tspan>
  </text>
  <line class="arrow-line" x1="894" y1="384" x2="894" y2="404"/>
  <polygon class="arrow-head" points="894,415 886,402 902,402"/>
  <circle cx="894" cy="470" r="52" fill="var(--disease)"/>
  <text class="outcome-label" x="894" y="477" text-anchor="middle">Disease</text>

  <g class="steps">
    <polygon class="step-edge" points="499,444 667,444 679,456 487,456"/>
    <rect class="step-box" x="499" y="421" width="168" height="23"/>
    <text class="step-label" x="583" y="440" text-anchor="middle">Therapies</text>

    <polygon class="step-edge" points="487,479 679,479 691,492 475,492"/>
    <rect class="step-box" x="487" y="456" width="192" height="23"/>
    <text class="step-label" x="583" y="475" text-anchor="middle">Prevention</text>

    <polygon class="step-edge" points="475,515 691,515 703,528 463,528"/>
    <rect class="step-box" x="475" y="492" width="216" height="23"/>
    <text class="step-label" x="583" y="511" text-anchor="middle">Critical targets</text>

    <polygon class="step-edge" points="463,551 703,551 715,564 451,564"/>
    <rect class="step-box" x="463" y="528" width="240" height="23"/>
    <text class="step-label" x="583" y="547" text-anchor="middle">Cellular machineries</text>

    <polygon class="step-edge" points="451,587 715,587 727,600 439,600"/>
    <rect class="step-box" x="451" y="564" width="264" height="23"/>
    <text class="step-label" x="583" y="583" text-anchor="middle">Disease models</text>

    <polygon class="step-edge" points="439,623 727,623 739,636 427,636"/>
    <rect class="step-box" x="439" y="600" width="288" height="23"/>
    <text class="step-label" x="583" y="619" text-anchor="middle">Cell, tissue &amp; organ responses</text>

    <rect class="step-box" x="427" y="636" width="312" height="24"/>
    <text class="step-label" x="583" y="655" text-anchor="middle">Mechanical force models</text>
  </g>
</svg>
</div>
</body>
</html>
```